Stationery Design Project for High End Wealth Management Firm

We need a stationery design for our high-end wealth management firm. Our clientele are affluent and our brand is built around providing investment services with world-class service.

The final concepts should provide a business card, letterhead, and envelope.

We like the idea of having text on the front and back and we MUST have black front and back business cards.
For the business card we have the following that needs to be included:
Company Logo & Tagline
Employee Name
Employee title
Employee Email
Website
2 seperate office cities, addresses, and phone numbers
Financial disclosure (small print)

Having black envelopes would be neat, but black is not a must for the envelopes.
Updates

Project Deadline Extended
Reason: To give the concept one more day of revisions.

Project Deadline Extended
Reason: To allow for more concepts and designs.

Target Market(s)

High Net Worth

Industry/Entity Type

Business

Requirements
Must have
• The following disclosure must be on the back of the card in small print:

Investment Advisory Services offered through Harrowgate Asset Partners LLC, a SEC Registered Investment Advisor. Corvane Wealth Management LLC is not affiliated with Harrowgate Asset Partners LLC.

Black business cards are also a must have.

Please utilize each of the 3 components of our logo in the design.

Please use our white background logo elements when designing our letterhead if you need them.
Nice to have
• Please use our company colors when designing. Utilize a combination of the elements of our logo that we have attached.

We are going to be printing our business cards on letterpress.

```html
<!DOCTYPE html>
<html lang="en">
<head>
<meta charset="utf-8">
<title>Corvane Wealth Management – Business Card</title>
<link rel="stylesheet" href="https://fonts.googleapis.com/css2?family=Arimo:wght@400;700&display=swap">
<style>
  :root {
    --backdrop: #3b3b3b;
    --card-black: #000000;
    --gold: #e2b23c;
    --gold-light: #f3cf6e;
    --gold-deep: #b67a1e;
    --white: #ffffff;
    --silver: #d9d9d9;
    --ink: #111111;
  }
  * { margin: 0; padding: 0; box-sizing: border-box; }
  html, body { width: 1200px; height: 534px; overflow: hidden; }
  body {
    background: var(--backdrop);
    font-family: "Arimo", Arial, sans-serif;
    position: relative;
  }
  .card {
    position: absolute;
    top: 117px;
    width: 525px;
    height: 299px;
    background: var(--card-black);
    border-radius: 22px;
    overflow: hidden;
    color: var(--white);
  }
  .card--back { left: 62px; }
  .card--front { left: 621px; }

  /* Back */
  .back-brand {
    position: absolute;
    top: 130px; left: 0; width: 100%;
    display: flex; justify-content: center; align-items: center; gap: 12px;
  }
  .brand-dot {
    width: 22px; height: 22px; border-radius: 50%;
    background: var(--gold);
    flex: none;
  }
  .brand-name {
    color: var(--gold);
    font-weight: 400;
    letter-spacing: 1px;
    text-transform: uppercase;
    white-space: nowrap;
  }
  .back-brand .brand-name { font-size: 24px; }
  .tagline {
    position: absolute;
    top: 216px; width: 100%;
    text-align: center;
    font-size: 10.5px;
    color: var(--white);
  }
  .disclosure {
    position: absolute;
    top: 260px; width: 100%;
    text-align: center;
    font-size: 7px;
    line-height: 10px;
    color: var(--silver);
  }

  /* Front */
  .front-brand {
    position: absolute;
    top: 58px; left: 36px;
    display: flex; align-items: center; gap: 10px;
  }
  .front-brand .brand-dot { width: 18px; height: 18px; }
  .front-brand .brand-name { font-size: 19px; }
  .contact {
    position: absolute;
    top: 146px; left: 36px;
    font-size: 12.5px;
    line-height: 15px;
  }
  .contact .label { color: var(--gold); }
  .contact .gap { height: 8px; }
  .contact .divider { color: var(--gold); }
  .person {
    position: absolute;
    top: 145px; right: 30px;
    text-align: right;
  }
  .person-name {
    color: var(--gold);
    font-size: 17px;
    letter-spacing: 0.5px;
    text-transform: uppercase;
  }
  .person-title { font-size: 12px; margin-top: 4px; }
  .gold-band {
    position: absolute;
    left: 0; right: 0; bottom: 0;
    height: 78px;
    background: linear-gradient(90deg, var(--gold-light) 0%, var(--gold) 50%, var(--gold-light) 78%, var(--gold-deep) 100%);
  }
  .website {
    position: absolute;
    right: 16px; top: 245px;
    color: var(--ink);
    font-size: 13px;
    letter-spacing: 1px;
  }
</style>
</head>
<body>

  <section class="card card--back">
    <div class="back-brand">
      <span class="brand-dot"></span>
      <span class="brand-name">Corvane Wealth Management</span>
    </div>
    <p class="tagline">Preferred Wealth Management for Select Individuals</p>
    <p class="disclosure">
      Investment Advisory Services offered through Harrowgate Asset Partners LLC, a SEC Registered Investment Advisor.<br>
      Corvane Wealth Management LLC is not affiliated with Harrowgate Asset Partners LLC
    </p>
  </section>

  <section class="card card--front">
    <div class="front-brand">
      <span class="brand-dot"></span>
      <span class="brand-name">Corvane Wealth Management</span>
    </div>

    <div class="contact">
      <p><span class="label">Office 1</span> office cities, addresses</p>
      <p><span class="label">Office 1</span> office cities, addresses</p>
      <div class="gap"></div>
      <p><span class="label">p :</span> 123 456 7888 <span class="divider">|</span> 123 456 7888</p>
      <p><span class="label">e :</span> danielwhitmore@corvane.com</p>
    </div>

    <div class="person">
      <p class="person-name">Daniel Whitmore</p>
      <p class="person-title">Position</p>
    </div>

    <div class="gold-band" role="img" aria-label="Decorative gold wave ornament along the bottom of the card"></div>
    <p class="website">www.corvane.com</p>
  </section>

</body>
</html>
```